Tallyden Web Design

Create Website Design for Tallyden. Tallyden is online application for collaboration team work system (task list management). More concept design for this project please find attach file ("tallyden website concept.pdf") . But my concept is just describe minimal features not bind design

For tallyden logo, i had already attach files. But i had not decided what color i chose, so it's okay if you suggest logo color for your suitable website design.
Updates

Dear All Designer,

I like brisk carousel (http://quillforge-labs.example/brisk-carousel/),
may be your concept design can adjust with this concept.
but don't worry about script for brisk carousel, my team will be handle
You just make website design to suitable with brisk carousel

but if you had own website design concept are welcome

thanks

Target Market(s)

Business Company

Industry/Entity Type

Management

```html
<!DOCTYPE html>
<html lang="en">
<head>
<meta charset="utf-8">
<title>Tallyden — Team Task Management</title>
<link rel="stylesheet" href="https://fonts.googleapis.com/css2?family=Baloo+2:wght@600;700&family=Ubuntu:wght@400;500&family=Kreon:wght@400;500&display=swap">
<style>
:root{
  --teal:#1d4f5c;
  --teal-dark:#163f49;
  --teal-light:#2f6a78;
  --green:#8ab322;
  --green-light:#a3c83a;
  --green-dark:#6e9417;
  --ink:#2b2b2b;
  --panel:#f6f6f6;
  --panel-edge:#e4e4e4;
  --footer:#3a3a3a;
}
*{box-sizing:border-box;margin:0;padding:0}
html,body{width:1200px;height:848px;overflow:hidden}
body{position:relative;background:#fff;font-family:"Ubuntu",sans-serif;color:var(--ink)}

.site-header{position:absolute;left:0;top:0;width:1200px;height:62px;background:linear-gradient(#ffffff,#f1f1f1)}
.brand{position:absolute;left:112px;top:8px;display:flex;align-items:center;gap:10px;font-family:"Ubuntu",sans-serif;font-weight:500;font-size:40px;color:var(--teal);letter-spacing:-0.5px}
.brand-dot{width:26px;height:26px;border-radius:50%;background:var(--green)}
.main-nav{position:absolute;left:340px;top:0;display:flex;height:62px}
.nav-home{width:56px;height:62px;background:#e9e9e9;display:flex;align-items:center;justify-content:center}
.nav-link{font-family:"Kreon",serif;font-size:17px;color:#333;line-height:62px;margin-left:18px;margin-right:18px;letter-spacing:.3px}
.login{position:absolute;left:1012px;top:20px;font-family:"Kreon",serif;font-size:17px;color:#333}
.login-ribbon{position:absolute;left:1058px;top:0}

.hero-band{position:absolute;left:0;top:62px;width:1200px;height:330px;background:linear-gradient(var(--teal-dark),var(--teal) 60%,#21596a)}

.panel{position:absolute;background:linear-gradient(#ffffff,var(--panel));border:1px solid var(--panel-edge);border-radius:7px;box-shadow:0 1px 3px rgba(0,0,0,.08)}
.showcase{left:100px;top:93px;width:668px;height:469px}
.showcase-media{position:absolute;left:14px;top:12px;width:638px;height:329px;background:linear-gradient(120deg,#c9cfd2,#8d8a83 45%,#5f6d4a 75%,#7f9c53)}
.play-button{position:absolute;left:253px;top:131px}
.showcase-title{position:absolute;left:0;top:352px;width:100%;text-align:center;font-family:"Baloo 2",sans-serif;font-weight:700;font-size:28px;color:var(--green)}
.showcase-text{position:absolute;left:64px;top:390px;width:540px;text-align:center;font-size:14.5px;line-height:22px;color:#222;letter-spacing:.6px}

.signup{left:788px;top:91px;width:298px;height:473px}
.signup-title{position:absolute;left:9px;top:14px;width:280px;font-family:"Baloo 2",sans-serif;font-weight:600;font-size:26px;line-height:31px;color:var(--teal)}
.signup-button{position:absolute;left:24px;top:121px;width:190px;height:48px;border-radius:24px;background:linear-gradient(var(--green-light),var(--green-dark));border:3px solid #e8efd6;box-shadow:0 1px 2px rgba(0,0,0,.25);font-family:"Kreon",serif;font-size:23px;color:#fff;text-align:center;line-height:42px;letter-spacing:1px}
.feature-list{position:absolute;left:9px;top:175px;list-style:none}
.feature-list li{height:32px;font-size:13px;color:#222;display:flex;align-items:center;gap:6px}

.feature-card{top:593px;height:194px}
.card-a{left:100px;width:329px}
.card-b{left:439px;width:329px}
.card-c{left:787px;width:299px}
.card-heading{position:absolute;left:8px;top:7px;right:8px;height:34px;border-radius:5px;background:linear-gradient(var(--teal-light),var(--teal-dark));color:#fff;font-family:"Baloo 2",sans-serif;font-weight:600;font-size:20px;line-height:36px;text-align:center}
.card-media{position:absolute;left:7px;top:54px;width:120px;height:120px}
.media-people{background:linear-gradient(135deg,#dcdcdc,#8a8f96 55%,#5a5e65)}
.media-device{left:12px;width:112px;height:118px;background:linear-gradient(135deg,#f4f4f4,#4e87c8 50%,#222)}
.media-typing{left:9px;width:116px;height:116px;background:linear-gradient(135deg,#e6eef2,#b7c4cc 60%,#7e8c95)}
.card-text{position:absolute;left:136px;top:54px;right:16px;font-size:11.5px;line-height:16px;text-align:justify;color:#222}
.card-b .card-text{left:132px}
.card-c .card-text{left:132px;right:8px}
.read-more{position:absolute;left:136px;top:149px;font-size:13px;font-weight:500;color:var(--teal)}
.card-b .read-more{left:132px}
.card-c .read-more{left:132px;top:151px}

.site-footer{position:absolute;left:0;top:818px;width:1200px;height:30px;background:var(--footer);color:#fff;font-family:Arial,sans-serif;font-size:12px;text-align:center;line-height:30px}
</style>
</head>
<body>
<header class="site-header">
  <div class="brand"><span>tallyden</span><span class="brand-dot"></span></div>
  <nav class="main-nav">
    <div class="nav-home">
      <svg width="26" height="24" viewBox="0 0 26 24" aria-label="Home">
        <path d="M13 2 L24 12 H21 V22 H5 V12 H2 Z" fill="var(--green)"/>
        <rect x="11" y="15" width="4" height="7" fill="#e9e9e9"/>
      </svg>
    </div>
    <span class="nav-link">About us</span>
    <span class="nav-link">Solutions</span>
    <span class="nav-link">Services</span>
    <span class="nav-link">Customers</span>
    <span class="nav-link">Contact Us</span>
  </nav>
  <span class="login">Login</span>
  <svg class="login-ribbon" width="24" height="52" viewBox="0 0 24 52">
    <path d="M0 0 H24 V42 L12 52 L0 42 Z" fill="var(--green)"/>
    <circle cx="12" cy="31" r="6" fill="var(--green-dark)"/>
    <text x="12" y="35" font-size="9" text-anchor="middle" fill="var(--green-light)" font-family="Ubuntu,sans-serif">1</text>
  </svg>
</header>

<div class="hero-band"></div>

<section class="panel showcase">
  <div class="showcase-media" role="img" aria-label="Photo of two colleagues smiling at a laptop in an office">
    <svg class="play-button" width="88" height="64" viewBox="0 0 88 64" aria-label="Play video">
      <rect width="88" height="64" rx="6" fill="#2a2a2a" opacity=".85"/>
      <path d="M33 14 L60 32 L33 50 Z" fill="#e8e8e8"/>
    </svg>
  </div>
  <h1 class="showcase-title">Simply dummy text of the typesetting.</h1>
  <p class="showcase-text">simply dummy text of the printing and typesetting industry. Lorem Ipsum has been Apps for SlatePad, PocketFone and Orbit Browser Integrated with Crateshare, Parcel and Skyfold Drive</p>
</section>

<aside class="panel signup">
  <h2 class="signup-title">Feel good about staying on top of Tallyden each day</h2>
  <div class="signup-button">Sign Up Now</div>
  <ul class="feature-list">
    <li><svg width="8" height="8" viewBox="0 0 8 8"><path d="M0 1 L3 4 L0 7 M4 1 L7 4 L4 7" stroke="var(--green)" stroke-width="1.5" fill="none"/></svg>Nothing to download, install or configure.</li>
    <li><svg width="8" height="8" viewBox="0 0 8 8"><path d="M0 1 L3 4 L0 7 M4 1 L7 4 L4 7" stroke="var(--green)" stroke-width="1.5" fill="none"/></svg>100% Web-based. Try it before you buy it.</li>
    <li><svg width="8" height="8" viewBox="0 0 8 8"><path d="M0 1 L3 4 L0 7 M4 1 L7 4 L4 7" stroke="var(--green)" stroke-width="1.5" fill="none"/></svg>Easy to use. Get started in minutes.</li>
    <li><svg width="8" height="8" viewBox="0 0 8 8"><path d="M0 1 L3 4 L0 7 M4 1 L7 4 L4 7" stroke="var(--green)" stroke-width="1.5" fill="none"/></svg>Feature-rich. Always less. More is great.</li>
    <li><svg width="8" height="8" viewBox="0 0 8 8"><path d="M0 1 L3 4 L0 7 M4 1 L7 4 L4 7" stroke="var(--green)" stroke-width="1.5" fill="none"/></svg>Start small &amp; scale up usage as needed.</li>
    <li><svg width="8" height="8" viewBox="0 0 8 8"><path d="M0 1 L3 4 L0 7 M4 1 L7 4 L4 7" stroke="var(--green)" stroke-width="1.5" fill="none"/></svg>Nothing to download, install or configure.</li>
    <li><svg width="8" height="8" viewBox="0 0 8 8"><path d="M0 1 L3 4 L0 7 M4 1 L7 4 L4 7" stroke="var(--green)" stroke-width="1.5" fill="none"/></svg>100% Web-based. Try it before you buy it.</li>
    <li><svg width="8" height="8" viewBox="0 0 8 8"><path d="M0 1 L3 4 L0 7 M4 1 L7 4 L4 7" stroke="var(--green)" stroke-width="1.5" fill="none"/></svg>Easy to use. Get started in minutes.</li>
  </ul>
</aside>

<article class="panel feature-card card-a">
  <h3 class="card-heading">Customize Application</h3>
  <div class="card-media media-people" role="img" aria-label="Photo of two coworkers reviewing documents at a desk"></div>
  <p class="card-text">simply dummy text of the printing industry typesetting industry. Lorem Ipsum has been the industry's standard dummy text ever since the 1500s,</p>
  <span class="read-more">read more..</span>
</article>

<article class="panel feature-card card-b">
  <h3 class="card-heading">Synchronize All Device</h3>
  <div class="card-media media-device" role="img" aria-label="Illustration of a smartphone with app icons floating out"></div>
  <p class="card-text">simply dummy text of the printing industry typesetting industry. Lorem Ipsum has been the industry's standard dummy text ever since the 1500s,</p>
  <span class="read-more">read more..</span>
</article>

<article class="panel feature-card card-c">
  <h3 class="card-heading">Report</h3>
  <div class="card-media media-typing" role="img" aria-label="Photo of hands typing on a keyboard beside a report"></div>
  <p class="card-text">simply dummy text of the printing industry typesetting industry. Lorem Ipsum has been the industry's standard dummy text ever since the 1500s,</p>
  <span class="read-more">read more..</span>
</article>

<footer class="site-footer">Copyright © 2012 Tallyden. All rights reserved.</footer>
</body>
</html>
```